Veltrane Application Brochures

Hi,

We are a semiconductor company looking to create application brochures to show a comprehensive overview of our product portfolio. The applications are as follows:
• Audio
• Automotive
• Proximity
• Smart Buildings
• Smartphones
• TV and Set-Top
• Wearables

To keep things consistent, we would like one template which we can use for the 7 application brochures listed above.

Our company website is:
https://www.veltrane-semiconductor.example/company/about-us

Veltrane Semiconductor provides highly integrated standard and custom mixed-signal ICs, optimized for smartphone, computing, IoT, SSL, and smart home applications.

Attaching what we had in the past for the "charging" application so you can see the type of information we will have.

Thank you

Marisol

```html
<!DOCTYPE html>
<html lang="en">
<head>
<meta charset="utf-8">
<title>Veltrane Semiconductor – Audio Application Brochure</title>
<link href="https://fonts.googleapis.com/css2?family=Open+Sans:wght@300;400;600;700&display=swap" rel="stylesheet">
<style>
  :root {
    --backdrop: #e9e4dc;
    --paper: #ffffff;
    --teal: #0aa3cc;
    --teal-deep: #0993bb;
    --teal-band: rgba(70, 178, 204, 0.88);
    --ink: #5c5c5c;
    --slate: #6f6f6f;
    --red: #d3283a;
    --red-dark: #a81827;
    --white: #ffffff;
  }
  * { box-sizing: border-box; margin: 0; padding: 0; }
  html, body {
    width: 1200px; height: 1200px; overflow: hidden;
    background: var(--backdrop);
    font-family: "Open Sans", Arial, sans-serif;
  }
  .brochure {
    position: absolute; left: 190px; top: 20px;
    width: 820px; height: 1160px;
    background: var(--paper);
    box-shadow: 0 4px 18px rgba(0,0,0,0.18);
    overflow: hidden;
  }
  .hero-photo {
    position: absolute; left: 0; top: 46px; width: 820px; height: 399px;
    background:
      radial-gradient(ellipse 30% 55% at 62% 45%, #6a4532 0%, rgba(106,69,50,0) 70%),
      radial-gradient(ellipse 35% 40% at 70% 90%, #4d9dc4 0%, rgba(77,157,196,0) 75%),
      linear-gradient(100deg, #f1c27d 0%, #e7a764 30%, #c98d5e 55%, #d9b08a 75%, #efd8b8 100%);
  }
  .hero-band {
    position: absolute; left: 0; top: 246px; width: 820px; height: 151px;
    background: var(--teal-band);
    color: var(--white);
  }
  .hero-title {
    position: absolute; left: 46px; top: 16px;
    font-weight: 300; font-size: 34px; line-height: 35px; letter-spacing: 0.3px;
  }
  .hero-subtitle {
    position: absolute; left: 46px; top: 90px;
    font-weight: 400; font-size: 16.5px; line-height: 18px;
  }
  .brand {
    position: absolute; left: 496px; top: 44px;
    display: flex; align-items: center; gap: 12px;
    color: var(--white); font-weight: 600;
  }
  .brand-dot { width: 48px; height: 48px; border-radius: 50%; background: var(--white); }
  .brand-name { font-size: 52px; line-height: 52px; letter-spacing: -1px; }
  .brand-sub { font-size: 12px; letter-spacing: 1.5px; display: block; margin-top: 2px; }

  .section-title {
    position: absolute; left: 0; top: 466px; width: 820px; text-align: center;
    color: var(--teal); font-weight: 600; font-size: 34px; line-height: 44px;
  }
  .intro {
    position: absolute; left: 48px; top: 520px; width: 724px; text-align: center;
    color: var(--ink); font-size: 19.5px; line-height: 21.6px;
  }

  .feature-list { position: absolute; left: 22px; top: 678px; width: 400px; }
  .feature { position: absolute; left: 0; width: 400px; }
  .feature-icon {
    position: absolute; left: 0; top: 0; width: 54px; height: 54px;
    border-radius: 50%;
    background: radial-gradient(circle at 40% 35%, #e8414f 0%, var(--red) 55%, var(--red-dark) 100%);
    border: 2px solid #8f8f8f;
    display: flex; align-items: center; justify-content: center;
  }
  .feature-body { position: absolute; left: 64px; top: 0; width: 336px; }
  .feature-name { color: var(--teal); font-size: 15px; line-height: 17px; }
  .feature-text { color: var(--ink); font-size: 15px; line-height: 16.8px; }

  .innovation {
    position: absolute; left: 433px; top: 682px; width: 363px; height: 360px;
    background: var(--slate); color: var(--white);
  }
  .innovation-head {
    background: var(--teal); height: 47px; padding: 0 0 0 23px;
    font-size: 19px; line-height: 47px; font-weight: 400;
  }
  .innovation-body { padding: 16px 14px 0 23px; font-size: 15px; line-height: 16.8px; }
  .innovation-body ul { list-style: none; }
  .innovation-body li { position: relative; padding-left: 23px; }
  .innovation-body li::before {
    content: ""; position: absolute; left: 3px; top: 5px;
    width: 8px; height: 8px; border-radius: 50%; background: var(--white);
  }

  .footer {
    position: absolute; left: 0; top: 1066px; width: 820px; height: 94px;
    background: var(--slate); color: var(--white);
    text-align: center; font-size: 17px; line-height: 23px; padding-top: 22px;
  }
  .footer strong { font-weight: 700; }
</style>
</head>
<body>
<main class="brochure">
  <div class="hero-photo" role="img" aria-label="Photo of a smiling young man in sunglasses and white headphones, holding a phone, in warm sunset light"></div>
  <section class="hero-band">
    <h1 class="hero-title">Powering the Smart<br>Connected Future</h1>
    <p class="hero-subtitle">Transforming analog fundamentals<br>into power efficient, connected solutions</p>
    <div class="brand">
      <span class="brand-dot"></span>
      <span><span class="brand-name">Veltrane</span><span class="brand-sub">SEMICONDUCTOR</span></span>
    </div>
  </section>

  <h2 class="section-title">Crystal clear audio</h2>
  <p class="intro">We offer a range of low power, hi-fi audio CODECs and class Ds with different features and packages suitable for a variety of low power, digital portable audio products. Our CODECs are designed to offer different levels of dynamic range<br>and improve the power consumption for the record and playback paths<br>by optimizing the always ON mode and utilizing efficient<br>charge pump technologies.</p>

  <section class="feature-list">
    <article class="feature" style="top:0">
      <div class="feature-icon">
        <svg width="26" height="28" viewBox="0 0 26 28" fill="none" stroke="#fff" stroke-width="2"><rect x="3" y="2" width="18" height="24" rx="2"/><path d="M11 19V9l6-2v9"/><circle cx="9.5" cy="19" r="1.8" fill="#fff"/><circle cx="15.5" cy="16" r="1.8" fill="#fff"/></svg>
      </div>
      <div class="feature-body">
        <h3 class="feature-name">Audio Codecs</h3>
        <p class="feature-text">Low power, Hi-Fi audio CODECs with different features and in packages suitable for a variety of digital and low power audio products.</p>
      </div>
    </article>
    <article class="feature" style="top:84px">
      <div class="feature-icon">
        <svg width="28" height="28" viewBox="0 0 28 28" fill="none" stroke="#fff" stroke-width="2.2"><path d="M5 20v-6a9 9 0 0 1 18 0v6"/><rect x="3" y="17" width="5" height="8" rx="1.5" fill="#fff"/><rect x="20" y="17" width="5" height="8" rx="1.5" fill="#fff"/><path d="M10 15a5 5 0 0 1 8 0M12 18a2 2 0 0 1 4 0"/></svg>
      </div>
      <div class="feature-body">
        <h3 class="feature-name">Wireless Audio</h3>
        <p class="feature-text">Our short range wireless ICs deliver enhanced efficiency to devices ranging from<br>DECT phones and wireless headsets to game controllers providing improved battery life.</p>
      </div>
    </article>
    <article class="feature" style="top:185px">
      <div class="feature-icon">
        <svg width="28" height="28" viewBox="0 0 28 28" fill="none" stroke="#fff" stroke-width="2.4"><path d="M5 17v-4a9 9 0 0 1 18 0v4"/><rect x="3" y="14" width="5" height="7" rx="1.5" fill="#fff"/><rect x="20" y="14" width="5" height="7" rx="1.5" fill="#fff"/><path d="M22 21c0 3-3 4-7 4"/></svg>
      </div>
      <div class="feature-body">
        <h3 class="feature-name">USB Audio</h3>
        <p class="feature-text">Our platform solutions range from low to high-end Linkra compliant USB headsets and headphones allowing development, software, and hardware resources to be shared across the product range.</p>
      </div>
    </article>
    <article class="feature" style="top:302px">
      <div class="feature-icon">
        <svg width="28" height="24" viewBox="0 0 28 24" fill="#fff"><rect x="2" y="4" width="24" height="16" fill="none" stroke="#fff" stroke-width="1.6"/><rect x="5" y="8" width="2.5" height="10"/><rect x="9.5" y="11" width="2.5" height="7"/><rect x="14" y="7" width="2.5" height="11"/><rect x="18.5" y="10" width="2.5" height="8"/></svg>
      </div>
      <div class="feature-body">
        <h3 class="feature-name">Audio Amplifiers</h3>
        <p class="feature-text">Powerful, highly efficient, low EMI mono filterless class D speaker driver ICs for 1S and 2S portable applications.</p>
      </div>
    </article>
  </section>

  <aside class="innovation">
    <h2 class="innovation-head">At the forefront of innovation</h2>
    <div class="innovation-body">
      <p>With a long legacy of delivering different power management designs for industry-leading mobile phone manufacturers and portable consumer OEMs, we optimize all aspects of design including electrical, thermal and packaging considerations. These designs offer unprecedented integration with multiple power management and analog functions on the chip, including:</p>
      <ul>
        <li>Programmable high-performance LDOs</li>
        <li>High-efficiency DC-DC voltage converters</li>
        <li>Intelligent battery charging circuits</li>
        <li>Software programmable LED drivers</li>
        <li>Sensor ADCs</li>
        <li>USB interfaces</li>
        <li>Integrated high performance, low power audio</li>
      </ul>
    </div>
  </aside>

  <footer class="footer">
    <p>42 Harrow Lane, Kestrel Park, Ashford AB1 2CD - United Kingdom</p>
    <p>Phone <strong>+44 (0) 1632 960418</strong> | Fax <strong>+44 (0) 1632 960733</strong> | Email <strong>info@veltrane.example</strong></p>
  </footer>
</main>
</body>
</html>
```